Business Card Design

Lintel PR is a public relations consultancy service for the self build, home refurbishment and home improvement market.
It represents everything about 'home' so envisage logo featuring maybe roof pitch over the 'A' of Lintel. Colour/font undecided.

Industry/Entity Type

Home Improvement

Contact Information for Business Card

Fenella Stroudwick
fenella@lintelpr-example.co.uk
Telephone Direct: 0700 555 0142

```html
<!DOCTYPE html>
<html lang="en">
<head>
<meta charset="utf-8">
<title>Lintel PR – Business Card</title>
<link rel="stylesheet" href="https://fonts.googleapis.com/css2?family=Questrial&display=swap">
<style>
  :root {
    --page-bg: #e6e7e8;
    --card-bg: #f7f7f5;
    --brand-blue: #1aa3dc;
    --ink: #1c1c1c;
    --ink-soft: #333333;
    --card-shadow: rgba(0, 0, 0, 0.18);
  }
  * { box-sizing: border-box; margin: 0; padding: 0; }
  html, body {
    width: 1200px;
    height: 1200px;
    overflow: hidden;
    background: var(--page-bg);
    font-family: "Questrial", "Century Gothic", sans-serif;
    color: var(--ink);
  }
  .canvas {
    width: 1200px;
    height: 1200px;
    display: flex;
    flex-direction: column;
    align-items: center;
    justify-content: center;
    gap: 70px;
  }
  .card {
    position: relative;
    width: 780px;
    height: 505px;
    background: var(--card-bg);
    box-shadow: 0 6px 22px var(--card-shadow);
    overflow: hidden;
  }

  /* Wordmark lockup */
  .wordmark {
    display: flex;
    flex-direction: column;
    align-items: flex-start;
  }
  .wordmark__name {
    display: flex;
    align-items: center;
    gap: 12px;
    font-size: 46px;
    letter-spacing: 2px;
    color: var(--ink);
    line-height: 1;
  }
  .wordmark__square {
    width: 22px;
    height: 22px;
    background: var(--brand-blue);
  }
  .wordmark__tagline {
    margin-top: 8px;
    font-size: 15px;
    letter-spacing: 0.6px;
    color: var(--ink-soft);
    text-transform: uppercase;
  }

  /* Back of card */
  .card--back {
    display: flex;
    align-items: center;
    justify-content: center;
  }
  .card--back .wordmark { align-items: center; }

  /* Front of card */
  .card--front .wordmark {
    position: absolute;
    left: 70px;
    top: 150px;
  }
  .contact {
    position: absolute;
    left: 440px;
    top: 110px;
  }
  .contact__name {
    font-size: 30px;
    color: var(--ink);
  }
  .contact__role {
    margin-top: 4px;
    font-size: 20px;
    color: var(--brand-blue);
  }
  .contact__list {
    list-style: none;
    margin-top: 56px;
  }
  .contact__item {
    display: flex;
    align-items: center;
    gap: 12px;
    font-size: 21px;
    color: var(--ink);
    margin-bottom: 22px;
  }
  .contact__icon {
    width: 24px;
    height: 24px;
    flex: none;
    fill: var(--brand-blue);
  }
  .swoosh {
    position: absolute;
    inset: 0;
    width: 100%;
    height: 100%;
    pointer-events: none;
  }
  .swoosh__blue { fill: var(--brand-blue); }
  .swoosh__gap { fill: var(--card-bg); }
  .swoosh__black { fill: var(--ink); }
</style>
</head>
<body>
<main class="canvas">

  <section class="card card--back" aria-label="Card back">
    <div class="wordmark">
      <div class="wordmark__name"><span class="wordmark__square"></span>LINTELPR</div>
      <div class="wordmark__tagline">Public Relations Consultancy</div>
    </div>
  </section>

  <section class="card card--front" aria-label="Card front">
    <div class="wordmark">
      <div class="wordmark__name"><span class="wordmark__square"></span>LINTELPR</div>
      <div class="wordmark__tagline">Public Relations Consultancy</div>
    </div>

    <div class="contact">
      <p class="contact__name">Fenella Stroudwick</p>
      <p class="contact__role">Consultant</p>
      <ul class="contact__list">
        <li class="contact__item">
          <svg class="contact__icon" viewBox="0 0 24 24" aria-hidden="true">
            <path d="M6.6 10.8a15.1 15.1 0 0 0 6.6 6.6l2.2-2.2c.3-.3.7-.4 1-.2 1.1.4 2.3.6 3.6.6.6 0 1 .4 1 1V20c0 .6-.4 1-1 1C10.6 21 3 13.4 3 4c0-.6.4-1 1-1h3.5c.6 0 1 .4 1 1 0 1.3.2 2.5.6 3.6.1.3 0 .7-.2 1L6.6 10.8z"/>
          </svg>
          0700 555 0142
        </li>
        <li class="contact__item">
          <svg class="contact__icon" viewBox="0 0 24 24" aria-hidden="true">
            <path d="M2 5h20v14H2V5zm2 2v.4l8 5.2 8-5.2V7H4zm16 2.8-8 5.2-8-5.2V17h16V9.8z"/>
          </svg>
          fenella@lintelpr-example.co.uk
        </li>
      </ul>
    </div>

    <svg class="swoosh" viewBox="0 0 780 505" preserveAspectRatio="none" aria-hidden="true">
      <path class="swoosh__blue" d="M0 340 C200 350 380 420 560 460 C660 482 730 490 780 488 L780 505 L0 505 Z"/>
      <path class="swoosh__gap" d="M280 392 C440 440 620 468 780 458 L780 480 C620 490 440 470 280 392 Z"/>
      <path class="swoosh__black" d="M380 412 C520 442 650 456 780 444 L780 464 C640 474 500 458 380 412 Z"/>
    </svg>
  </section>

</main>
</body>
</html>
```